Children's Educational Software - Login Screens

We need graphics for some basic login pages. The main requirements are a background image, buttons and background overlay (box for login fields and app icons). Must utilize responsive design for various resolutions and devices. The mock-up file provides an example of the direction we are wanting to go. The app page will require a version of the background that extends down using a solid colour. One idea would be to add some flowers, bees, etc. to help add some life to the bottom half. I like the idea of clouds and grass, but am open to anything.

Target Market(s)

Elementary teachers and young children

Coding

Coded - Design and coding required

Number of Pages Required

2 page

Font styles to use
Sans Serif

Requirements
Must have
• Responsive design for various resolutions and devices
Nice to have
• clouds, grass, new app icons if current icons don't fit with new design

```html
<!DOCTYPE html>
<html lang="en">
<head>
<meta charset="utf-8">
<title>School Login</title>
<link rel="stylesheet" href="https://fonts.googleapis.com/css2?family=Roboto:wght@400;500;700&display=swap">
<style>
  :root {
    --sky-top: #0596dd;
    --sky-bottom: #35bff9;
    --panel-white: #ffffff;
    --header-yellow: #f9d31c;
    --title-ink: #2d2a1e;
    --label-blue: #4a6f8f;
    --field-border: #c9cdd2;
    --accent-orange: #ee764c;
    --link-lilac: #8c8fd8;
    --divider-grey: #c8c8c8;
    --footer-ink: #eaf7ff;
    --art-tone: rgba(255, 255, 255, 0.16);
    --art-tone-deep: rgba(12, 60, 110, 0.12);
  }
  * { box-sizing: border-box; margin: 0; padding: 0; }
  html, body { width: 1200px; height: 675px; overflow: hidden; }
  body {
    font-family: "Roboto", sans-serif;
    background: linear-gradient(135deg, var(--sky-top) 0%, var(--sky-bottom) 100%);
    position: relative;
  }

  .climber-art {
    position: absolute;
    top: 0;
    border-radius: 0 0 40px 40px;
    background: linear-gradient(180deg, var(--art-tone-deep) 0%, var(--art-tone) 100%);
  }
  .climber-art--one   { left: 66px;  width: 119px; height: 303px; }
  .climber-art--two   { left: 237px; width: 130px; height: 417px; }
  .climber-art--three { left: 415px; width: 90px;  height: 230px; }
  .climber-art--four  { left: 778px; width: 100px; height: 373px; }
  .climber-art--five  { left: 883px; width: 151px; height: 426px; }

  .login-card {
    position: absolute;
    left: 460px;
    top: 265px;
    width: 280px;
    height: 297px;
    background: var(--panel-white);
    border-radius: 4px;
    box-shadow: 0 2px 8px rgba(0, 40, 80, 0.18);
    overflow: hidden;
  }
  .login-card__header {
    height: 53px;
    background: var(--header-yellow);
    display: flex;
    align-items: center;
    justify-content: center;
  }
  .login-card__title {
    font-size: 20px;
    font-weight: 500;
    color: var(--title-ink);
  }
  .login-form { padding: 33px 0 0 24px; }
  .login-form__row {
    display: flex;
    align-items: center;
    margin-bottom: 21px;
  }
  .login-form__label {
    width: 65px;
    font-size: 10px;
    font-weight: 700;
    color: var(--label-blue);
  }
  .login-form__input {
    width: 163px;
    height: 26px;
    border: 1px solid var(--field-border);
    border-radius: 4px;
    background: var(--panel-white);
  }
  .login-form__submit {
    display: block;
    margin: 2px 0 0 50px;
    width: 132px;
    height: 26px;
    border: none;
    border-radius: 13px;
    background: var(--accent-orange);
    color: var(--panel-white);
    font-family: "Roboto", sans-serif;
    font-size: 10px;
    font-weight: 700;
    box-shadow: 0 2px 4px rgba(0, 0, 0, 0.2);
  }
  .login-card__divider {
    position: absolute;
    left: 8px;
    right: 8px;
    top: 245px;
    border: none;
    border-top: 1px solid var(--divider-grey);
  }
  .login-card__links {
    position: absolute;
    top: 265px;
    left: 0;
    right: 0;
    display: flex;
    justify-content: center;
    gap: 25px;
    font-size: 12.5px;
  }
  .login-card__links a { color: var(--link-lilac); text-decoration: underline; }

  .role-switch {
    position: absolute;
    left: 1129px;
    top: 300px;
    display: flex;
    flex-direction: column;
    gap: 22px;
    list-style: none;
  }
  .role-switch__item {
    width: 46px;
    display: flex;
    flex-direction: column;
    align-items: center;
    color: var(--panel-white);
    font-size: 12.5px;
  }
  .role-switch__icon {
    width: 46px;
    height: 33px;
    background: var(--accent-orange);
    box-shadow: 0 1px 3px rgba(0, 0, 0, 0.2);
    display: flex;
    align-items: center;
    justify-content: center;
    margin-bottom: 3px;
  }

  .site-footer {
    position: absolute;
    left: 0;
    right: 0;
    top: 646px;
    text-align: center;
    font-size: 12px;
    color: var(--footer-ink);
  }
</style>
</head>
<body>
  <div class="climber-art climber-art--one" role="img" aria-label="Cartoon child swinging on a rope"></div>
  <div class="climber-art climber-art--two" role="img" aria-label="Cartoon child in a cap climbing a rope"></div>
  <div class="climber-art climber-art--three" role="img" aria-label="Cartoon girl with glasses climbing a rope"></div>
  <div class="climber-art climber-art--four" role="img" aria-label="Cartoon girl climbing a rope"></div>
  <div class="climber-art climber-art--five" role="img" aria-label="Cartoon child with curly hair climbing a rope"></div>

  <main class="login-card">
    <header class="login-card__header">
      <h1 class="login-card__title">School Login</h1>
    </header>
    <form class="login-form">
      <div class="login-form__row">
        <label class="login-form__label" for="student-id">STUDENT ID</label>
        <input class="login-form__input" id="student-id" type="text">
      </div>
      <div class="login-form__row">
        <label class="login-form__label" for="password">PASSWORD</label>
        <input class="login-form__input" id="password" type="password">
      </div>
      <button class="login-form__submit" type="button">LOGIN</button>
    </form>
    <hr class="login-card__divider">
    <nav class="login-card__links">
      <a href="#">Support Page</a>
      <a href="#">Quick Start Guide</a>
    </nav>
  </main>

  <ul class="role-switch">
    <li class="role-switch__item">
      <span class="role-switch__icon">
        <svg width="24" height="22" viewBox="0 0 24 22" fill="#fff">
          <circle cx="12" cy="4" r="3.2"/>
          <path d="M12 9c-2 0-3.5 1-3.5 3v2h7v-2c0-2-1.5-3-3.5-3z"/>
          <path d="M2 12c4 0 7 1 10 3 3-2 6-3 10-3v8c-4 0-7 1-10 2-3-1-6-2-10-2z" fill="none" stroke="#fff" stroke-width="1.6"/>
        </svg>
      </span>
      Student
    </li>
    <li class="role-switch__item">
      <span class="role-switch__icon">
        <svg width="26" height="22" viewBox="0 0 26 22" fill="#fff">
          <rect x="9" y="2" width="15" height="11" fill="none" stroke="#fff" stroke-width="1.5"/>
          <circle cx="5" cy="5" r="2.6"/>
          <path d="M2 9h6l5-3 1 1-5 4v11H6v-6H4v6H2z"/>
        </svg>
      </span>
      Teacher
    </li>
    <li class="role-switch__item">
      <span class="role-switch__icon">
        <svg width="24" height="24" viewBox="0 0 24 24" fill="#fff">
          <circle cx="7" cy="6" r="3.4" fill="none" stroke="#fff" stroke-width="2" stroke-dasharray="2 1.5"/>
          <circle cx="15" cy="10" r="3.6"/>
          <path d="M8 23c0-5 3-8 7-8s7 3 7 8z"/>
        </svg>
      </span>
      Admin
    </li>
  </ul>

  <footer class="site-footer">Bright Steps Learning © 2019 • Support: 1-800-555-0142</footer>
</body>
</html>
```